TRV Advisory Business Cards

Hi there,

I'd like to make a simple new business card design with the logo we already have created for our business.

I need a double sided business card with our logo on the front side and the company and person's details on the back side.

I'd like it to be on a white background and no background so I can potentially use it with either white paper or put it on different coloured paper in accordance with our business colours.

Please use the logo images I have attached and also the fonts.

So Front side:
- Logo in centre of business card (use medium logo so there is a pretty decent border around it, so don't want to fill the whole card but to make it prominent).

Back Side.
- We need 3 different business cards with the different people's name on each.

ie.

Dariel Moratkin
Business Development Manager

m +61 437 290 618
e dariel@trvadvisory.com.au
w trvadvisory.com.au

- Also I'd like to put only the cog/power button logo in the top right hand corner of the card.
(You might need to chop the current logo in half as I don't have a seperate log just for this)
- Also I'd like some lines running on the top left hand corner diagonally, anything that will add to the design or some swirling lines that add some cool effect to the card.

Also I'd like to maybe put our ABN in the bottom right hand corner of the card in a smaller font.

I'd like to also talk to the designer if possible so I can get my idea across a bit better.

Thanks!

Regards,
Dariel

```html
<!DOCTYPE html>
<html lang="en">
<head>
<meta charset="utf-8">
<title>TRV Advisory Business Cards</title>
<link rel="stylesheet" href="https://fonts.googleapis.com/css2?family=Michroma&family=Montserrat:wght@500;600;700&display=swap">
<style>
  :root {
    --stage: #e6e6e6;
    --card: #ffffff;
    --ink: #3d3d3d;
    --ink-soft: #6b6b6b;
    --accent: #f29a1f;
    --accent-light: #fbd27a;
    --badge: #454545;
  }
  * { box-sizing: border-box; margin: 0; padding: 0; }
  html, body {
    width: 1200px;
    height: 840px;
    overflow: hidden;
    background: var(--stage);
  }
  .sheet {
    position: relative;
    width: 1200px;
    height: 840px;
  }
  .card {
    position: absolute;
    top: 270px;
    width: 520px;
    height: 300px;
    background: var(--card);
    box-shadow: 0 2px 10px rgba(0,0,0,0.12);
    overflow: hidden;
  }
  .card--front { left: 50px; }
  .card--back { left: 630px; }

  .swirl {
    position: absolute;
    background: radial-gradient(ellipse at 20% 20%, rgba(251,210,122,0.65), rgba(242,154,31,0.15) 60%, rgba(255,255,255,0) 75%);
  }
  .card--front .swirl { left: 0; top: 0; width: 190px; height: 130px; }
  .card--back .swirl {
    right: 0; top: 0; width: 230px; height: 110px;
    background: radial-gradient(ellipse at 80% 10%, rgba(251,210,122,0.7), rgba(242,154,31,0.18) 60%, rgba(255,255,255,0) 75%);
  }

  .brand {
    position: absolute;
    left: 0; right: 0; top: 118px;
    display: flex;
    align-items: center;
    justify-content: center;
    gap: 12px;
  }
  .brand__dot {
    width: 44px; height: 44px;
    border-radius: 50%;
    background: var(--badge);
  }
  .brand__block { display: flex; flex-direction: column; }
  .brand__name {
    font-family: "Montserrat", sans-serif;
    font-weight: 700;
    font-size: 34px;
    line-height: 1;
    color: var(--ink);
    letter-spacing: -0.5px;
  }
  .brand__tagline {
    margin-top: 4px;
    font-family: "Montserrat", sans-serif;
    font-weight: 600;
    font-size: 8.5px;
    letter-spacing: 2.2px;
    color: var(--ink);
    white-space: nowrap;
  }

  .badge {
    position: absolute;
    left: 52px; top: 64px;
    width: 160px;
    display: flex;
    flex-direction: column;
    align-items: center;
    gap: 10px;
  }
  .badge__circle {
    width: 132px; height: 132px;
    border-radius: 50%;
    background: var(--badge);
  }
  .badge__name {
    font-family: "Montserrat", sans-serif;
    font-weight: 700;
    font-size: 15px;
    color: var(--ink);
  }

  .person {
    position: absolute;
    left: 262px; top: 96px;
    width: 230px;
  }
  .person__name {
    font-family: "Michroma", sans-serif;
    font-size: 16px;
    font-weight: 400;
    color: var(--ink);
    letter-spacing: 0.5px;
    text-transform: uppercase;
    white-space: nowrap;
  }
  .person__role {
    margin-top: 4px;
    padding-bottom: 6px;
    border-bottom: 1px solid var(--ink-soft);
    font-family: "Montserrat", sans-serif;
    font-weight: 600;
    font-size: 8.5px;
    letter-spacing: 1.4px;
    color: var(--accent);
    text-transform: uppercase;
    white-space: nowrap;
  }
  .contacts {
    list-style: none;
    margin-top: 26px;
    display: flex;
    flex-direction: column;
    gap: 9px;
  }
  .contacts__item {
    display: flex;
    align-items: center;
    gap: 9px;
    font-family: "Michroma", sans-serif;
    font-size: 8.5px;
    color: var(--ink);
    letter-spacing: 0.6px;
    text-transform: uppercase;
    white-space: nowrap;
  }
  .contacts__icon { width: 12px; height: 12px; flex: none; }

  .abn {
    position: absolute;
    left: 28px; bottom: 20px;
    font-family: "Michroma", sans-serif;
    font-size: 7.5px;
    letter-spacing: 0.8px;
    color: var(--ink);
  }
</style>
</head>
<body>
<main class="sheet">

  <section class="card card--front" aria-label="Business card front">
    <div class="swirl" role="img" aria-label="Flowing orange swirl lines in the top left corner"></div>
    <div class="brand">
      <span class="brand__dot"></span>
      <div class="brand__block">
        <span class="brand__name">TRV Advisory</span>
        <span class="brand__tagline">PRACTICAL ADVICE. REAL RESULTS</span>
      </div>
    </div>
  </section>

  <section class="card card--back" aria-label="Business card back">
    <div class="swirl" role="img" aria-label="Flowing orange swirl lines in the top right corner"></div>

    <div class="badge">
      <span class="badge__circle"></span>
      <span class="badge__name">TRV Advisory</span>
    </div>

    <div class="person">
      <h1 class="person__name">Dariel Moratkin</h1>
      <p class="person__role">Business Development Manager</p>
      <ul class="contacts">
        <li class="contacts__item">
          <svg class="contacts__icon" viewBox="0 0 12 12" aria-hidden="true">
            <rect x="3" y="0.5" width="6" height="11" rx="1" fill="none" stroke="var(--accent)" stroke-width="1.2"/>
            <rect x="5" y="9" width="2" height="1" fill="var(--accent)"/>
          </svg>
          +61 437 290 618
        </li>
        <li class="contacts__item">
          <svg class="contacts__icon" viewBox="0 0 12 12" aria-hidden="true">
            <rect x="0.6" y="2.5" width="10.8" height="7.5" fill="none" stroke="var(--accent)" stroke-width="1.2"/>
            <path d="M0.8 2.8 L6 7 L11.2 2.8" fill="none" stroke="var(--accent)" stroke-width="1.2"/>
          </svg>
          dariel@trvadvisory.com.au
        </li>
        <li class="contacts__item">
          <svg class="contacts__icon" viewBox="0 0 12 12" aria-hidden="true">
            <circle cx="6" cy="6" r="5.2" fill="none" stroke="var(--accent)" stroke-width="1.2"/>
            <ellipse cx="6" cy="6" rx="2.2" ry="5.2" fill="none" stroke="var(--accent)" stroke-width="1"/>
            <line x1="0.8" y1="6" x2="11.2" y2="6" stroke="var(--accent)" stroke-width="1"/>
          </svg>
          trvadvisory.com.au
        </li>
      </ul>
    </div>

    <p class="abn">ABN : 5127 8830 492</p>
  </section>

</main>
</body>
</html>
```